Company email signature, make it look perfect!

make my signature high resolution, and ready for use as a outlook email signature
Look at the doc below ' this is what im looking to achieve.
The key items are - make this all high resolution with the actual images below used. Make the signature all the same colour.
If you want to make the signature look better than it does, with the layout below. It has to incorporate everything in the ' this is what im trying to achieve doc'
The order of the brands below 'Forma Construction Group' are to go in the order : Stonerise , Commercial Builders Kestrelton, Kestrelton Renovation builders, builders kestrelton
Forma Construction Group Signature

```html
<!DOCTYPE html>
<html lang="en">
<head>
<meta charset="utf-8">
<title>Forma Construction Group – Email Signature</title>
<link href="https://fonts.googleapis.com/css2?family=Montserrat:wght@500;600;700&display=swap" rel="stylesheet">
<style>
  :root {
    --backdrop: #5b5b5d;
    --paper: #ffffff;
    --ink: #0d0d0d;
    --brand-navy: #1f2d3f;
    --rule: #d4d4d4;
    --footer-band: #000000;
  }
  * { box-sizing: border-box; margin: 0; padding: 0; }
  html, body {
    width: 1200px; height: 960px; overflow: hidden;
    background: var(--backdrop);
    font-family: "Montserrat", Arial, sans-serif;
  }
  .signature {
    position: absolute; left: 99px; top: 309px;
    width: 1002px; height: 341px;
    background: var(--paper);
  }
  .signature-head {
    position: absolute; left: 0; top: 0; width: 100%; height: 157px;
    border-bottom: 3px solid var(--rule);
  }
  .company-mark {
    position: absolute; left: 26px; top: 38px;
    display: flex; align-items: center; gap: 14px;
  }
  .company-mark .mark-square {
    width: 44px; height: 44px; background: var(--ink);
  }
  .company-mark .company-name {
    font-size: 27px; font-weight: 500; line-height: 1.12; color: var(--ink);
    text-transform: uppercase; width: 260px;
  }
  .head-divider {
    position: absolute; top: 61px; width: 2px; height: 72px;
    background: var(--rule);
  }
  .head-divider.first { left: 377px; }
  .head-divider.second { left: 625px; }
  .person {
    position: absolute; left: 403px; top: 84px; color: var(--ink);
  }
  .person-name { font-size: 18px; font-weight: 700; letter-spacing: 0.2px; }
  .person-role { font-size: 15px; font-weight: 600; margin-top: 4px; letter-spacing: 0.3px; }
  .contact-list {
    position: absolute; left: 653px; top: 60px; list-style: none;
  }
  .contact-list li {
    display: flex; align-items: center; gap: 9px;
    font-size: 15.5px; font-weight: 600; color: var(--ink);
    height: 23px; letter-spacing: 0.2px;
  }
  .contact-list svg { width: 19px; height: 19px; flex: none; }
  .brand-row {
    position: absolute; left: 0; top: 160px; width: 100%; height: 165px;
    display: flex;
  }
  .brand-cell {
    display: flex; align-items: center; justify-content: center;
    text-align: center; color: var(--brand-navy);
    font-weight: 700; text-transform: uppercase; line-height: 1.12;
    position: relative;
  }
  .brand-cell + .brand-cell::before {
    content: ""; position: absolute; left: 0; top: 6px; bottom: 12px;
    width: 2px; background: var(--rule);
  }
  .brand-cell.stonerise { width: 228px; font-size: 34px; text-transform: none; }
  .brand-cell.commercial { width: 247px; font-size: 24px; }
  .brand-cell.renovation { width: 246px; font-size: 21px; }
  .brand-cell.builders { width: 281px; font-size: 27px; }
  .footer-band {
    position: absolute; left: 0; bottom: 0; width: 100%; height: 16px;
    background: var(--footer-band);
  }
</style>
</head>
<body>
  <section class="signature">
    <header class="signature-head">
      <div class="company-mark">
        <span class="mark-square"></span>
        <span class="company-name">Forma Construction Group</span>
      </div>
      <span class="head-divider first"></span>
      <div class="person">
        <p class="person-name">Jonah Whitfield</p>
        <p class="person-role">Managing Director</p>
      </div>
      <span class="head-divider second"></span>
      <ul class="contact-list">
        <li>
          <svg viewBox="0 0 20 20" aria-hidden="true"><circle cx="10" cy="10" r="10" fill="#0d0d0d"/><path d="M7 5.2c.5-.3 1-.2 1.3.3l.9 1.6c.2.4.1.9-.3 1.2l-.6.4c.4 1 1.3 2 2.3 2.5l.5-.6c.3-.4.8-.5 1.2-.2l1.5 1c.4.3.5.8.2 1.2l-.5.7c-.4.5-1.1.7-1.700.5-2.6-.9-4.600-3-5.4-5.6-.2-.6 0-1.3.5-1.700z" fill="#fff"/></svg>
          022 555 0187
        </li>
        <li>
          <svg viewBox="0 0 20 20" aria-hidden="true"><circle cx="10" cy="10" r="10" fill="#0d0d0d"/><g fill="none" stroke="#fff" stroke-width="1.1"><circle cx="10" cy="10" r="5"/><ellipse cx="10" cy="10" rx="2.2" ry="5"/><path d="M5 10h10M5.8 7.5h8.4M5.8 12.5h8.4"/></g></svg>
          www.formaconstructiongroup.co.nz
        </li>
        <li>
          <svg viewBox="0 0 20 20" aria-hidden="true"><circle cx="10" cy="10" r="10" fill="#0d0d0d"/><g fill="none" stroke="#fff" stroke-width="1.2"><rect x="5" y="6.5" width="10" height="7.5" rx="1"/><path d="M5.3 7l4.7 3.8L14.7 7"/></g></svg>
          jonah@formaconstructiongroup.com
        </li>
      </ul>
    </header>

    <div class="brand-row">
      <div class="brand-cell stonerise">Stonerise</div>
      <div class="brand-cell commercial">Commercial<br>Builders<br>Kestrelton</div>
      <div class="brand-cell renovation">Kestrelton<br>Renovation<br>Builders</div>
      <div class="brand-cell builders">Builders<br>Kestrelton</div>
    </div>

    <div class="footer-band"></div>
  </section>
</body>
</html>
```